Tallowfern Letterheads Design

Hello, we have just upgraded this project for a guaranteed payment.

We are currently going through a re-branding exercise internally. Our logo is attached as a PDF file.

We are happy with our logo but would like to investigate how we can best apply the logo to our letterheads and compliment slips.

We are a quality printing company in England. Despite our name we are very professional and offer a personal service.

Our new website is under construction and here is a link to show you how it looks: http://tallowpress.marlwood.co.uk

The style must be professional and steer away from "tacky" otherwise it makes our company look very low budget and just a bit silly.

We would like to see elements of creativity though, so please, nothing too boring.

I have attached our new logo, there is an option for use on white or black.

Cheers
Tallowfern Team
Updates

Project Deadline Extended
Reason: We have increased the deadline due to an internal delay to things, we now have more time before we need anything to be printed.

Industry/Entity Type

Construction

Requirements
Must have
• IMPORTANT! Please do not tweak or change our logo in any way. A few designs show vast changes in the logo, this is not what we require. Please do not change the logo in any way. Thanks
Nice to have
• Classy but approachable. Elements of "quirky" would be nice to see.
Should not have
• A Tacky feel

```html
<!DOCTYPE html>
<html lang="en">
<head>
<meta charset="utf-8">
<title>Tallowfern Letterhead</title>
<link rel="stylesheet" href="https://fonts.googleapis.com/css2?family=Arimo:wght@400;700&display=swap">
<style>
  :root {
    --backdrop: #c9c9c9;
    --paper: #ffffff;
    --brand-pink: #e5005a;
    --soft-pink: #f08cb8;
    --ink: #1f1f1f;
    --logo-black: #141414;
    --sheep-grey: #8f8f8f;
  }
  * { box-sizing: border-box; margin: 0; padding: 0; }
  html, body { width: 1200px; height: 900px; overflow: hidden; }
  body {
    background: var(--backdrop);
    font-family: "Arimo", Arial, sans-serif;
    color: var(--ink);
    position: relative;
  }
  .letterhead {
    position: absolute;
    left: 343px; top: 72px;
    width: 541px; height: 754px;
    background: var(--paper);
    overflow: hidden;
  }
  .top-band {
    position: absolute; left: 0; top: 0;
    width: 100%; height: 6px;
    background: var(--brand-pink);
  }
  .logo-block {
    position: absolute;
    left: 55px; top: 0;
    width: 152px; height: 117px;
    background: var(--logo-black);
    display: flex; align-items: center; justify-content: center;
    gap: 6px;
    padding-top: 28px;
  }
  .logo-dot {
    width: 10px; height: 10px; border-radius: 50%;
    background: var(--brand-pink);
  }
  .logo-name {
    color: #fff;
    font-weight: 700;
    font-size: 19px;
    letter-spacing: -0.3px;
  }
  .letter-body {
    position: absolute;
    left: 65px; top: 154px;
    width: 412px;
    font-size: 8.3px;
    line-height: 10.2px;
  }
  .letter-body p { margin-bottom: 10.2px; }
  .contact {
    position: absolute;
    top: 671px;
    font-size: 8.6px;
    line-height: 10.6px;
  }
  .contact--phone { left: 54px; }
  .contact--address { left: 203px; font-weight: 700; }
  .contact .label { color: var(--brand-pink); font-weight: 700; }
  .corner-illustration {
    position: absolute;
    right: 0; bottom: 0;
    width: 216px; height: 116px;
  }
</style>
</head>
<body>
  <main class="letterhead">
    <div class="top-band"></div>

    <div class="logo-block">
      <span class="logo-dot"></span>
      <span class="logo-name">Tallowfern</span>
    </div>

    <section class="letter-body">
      <p>Lorem ipsum,</p>
      <p>dolor sit amet, consectetur adipiscing elit. Cras rutrum aliquam vehicula. Nullam malesuada purus id quam mattis, eget scelerisque leo facilisis. Fusce egestas pellentesque nisl id egestas. Lorem ipsum dolor sit amet, consectetur adipiscing elit. Vivamus pulvinar risus hendrerit velit accumsan viverra. Donec a orci congue, mollis ligula quis, porta elit. Nulla felis sapien, mattis quis vestibulum ac, ullamcorper id magna. Vestibulum magna nulla, facilisis nec gravida sit amet, mattis ut enim. Ut pretium pharetra magna, id cursus ligula tincidunt nec. Curabitur mattis, nibh a vestibulum pharetra, dolor tellus elementum est, id cursus leo velit vitae diam. Suspendisse quis turpis ac magna euismod semper. Vestibulum et velit in ligula lobortis laoreet. Nullam ac hendrerit quam. Mauris nec sollicitudin urna.</p>
      <p>Integer in elit rutrum, semper enim et, convallis orci. Etiam risus metus, pellentesque sit amet ornare et, hendrerit ac nunc. Ut lacinia dui magna, at hendrerit tortor commodo in. Praesent eget dignissim sem. Vestibulum ullamcorper volutpat ultricies. Sed tempus, magna at fringilla pulvinar, lorem orci condimentum dui, sit amet tempor libero lacus at eros. Curabitur auctor mauris tristique elit aliquam, ac ultricies sem blandit. Ut leo felis, egestas eget tempus sit amet, fermentum non sem. Nullam eu hendrerit neque, a porttitor nisl. Class aptent taciti sociosqu ad litora torquent per conubia nostra, per inceptos himenaeos.</p>
      <p>Vivamus gravida nisi non rhoncus convallis. Suspendisse dui dolor, facilisis et justo vitae, placerat gravida lectus. Suspendisse ut dignissim mauris. Interdum et malesuada fames ac ante ipsum primis in faucibus. Curabitur vel lacinia leo. Sed et convallis enim. Ut eleifend, orci consequat dapibus vestibulum, dui mi venenatis nisi, eget laoreet diam lectus vel est. Sed feugiat ante eu pharetra mattis. Duis ut turpis pretium, congue sapien sed, gravida nibh. Aliquam nec purus ut est porttitor faucibus nec id magna. Sed ac dolor consequat, aliquet nibh eget, rhoncus felis. Vivamus nisl lectus, adipiscing vel semper sed, suscipit sed leo.</p>
      <p>Integer quis porta nibh. Nulla porta gravida odio eu ullamcorper. Donec feugiat tincidunt aliquet. Proin consectetur odio mauris, sed vehicula purus accumsan id. Donec nisi leo, congue quis sapien quis, semper tincidunt lacus. Sed lobortis enim in condimentum congue. Suspendisse potenti. Nulla quam diam, rutrum at sapien viverra, faucibus dapibus magna. Vestibulum sollicitudin dignissim velit, et rutrum sapien sollicitudin sit amet. Donec sit amet varius turpis. Donec volutpat eleifend nisl in auctor. Donec id scelerisque ipsum. Duis porttitor, mi eu congue bibendum, nulla ipsum lacinia turpis, vel semper orci ligula a quam. Donec vulputate sodales tempus. Vivamus quis quam metus.</p>
      <p>Aenean velit orci, porta at nibh ac, sagittis ultrices magna. Sed cursus convallis lacus, vel aliquet sem ullamcorper venenatis. Curabitur ac orci in nunc rhoncus placerat. Integer eu rutrum mauris, dictum cursus dolor. Aenean fringilla eros at dolor tincidunt pellentesque vitae quis diam. Fusce sit amet mi auctor, interdum augue vel, porttitor dolor.</p>
      <p>Maecenas porta pretium venenatis</p>
    </section>

    <address class="contact contact--phone" style="font-style:normal">
      <span class="label">| Tel:</span> 0208 555 0187<br>
      <span class="label">| Email:</span> sales@tallowfern.co.uk
    </address>

    <address class="contact contact--address" style="font-style:normal">
      <span class="label">| Address:</span><br>
      17 Mill Lane,<br>
      Ashby-Under-Wold,<br>
      Ashby,<br>
      Kent,<br>
      TN9 4QX
    </address>

    <svg class="corner-illustration" viewBox="0 0 216 116" role="img" aria-label="Brand mascot illustration peeking in from the bottom-right corner">
      <defs>
        <linearGradient id="mascotTone" x1="0" y1="0" x2="1" y2="1">
          <stop offset="0" stop-color="#a3a3a3"/>
          <stop offset="1" stop-color="#f08cb8"/>
        </linearGradient>
      </defs>
      <rect x="0" y="0" width="216" height="116" rx="40" fill="url(#mascotTone)" opacity="0.85"/>
    </svg>
  </main>
</body>
</html>
```